Venture Capital firm needs modern business cards

We are a Venture Capital firm within financial services/Asset management. The industry generally has basic business cards with black, blue and maybe green/yellow design elements.
Our firm has a four-colour swoosh logo. We are based in London and want to stand out, just a little bit!, from the crowd. Our company is called ROLK Investments and the 'C' stands for collaboration thus using artfolkhub is a natural portal for our business card design competition. Our logo came via artfolkhub too!
We use 'Venture Partner in Asset Management' as our tagline and this is Trademark registered. We operate in a conservative industry and we should not overstep our mark. The logo is colorful as it is and therefore the rest of the design should not be too fanciful.
The objective is twofold: make our logo element stick and memorable with our audience, whilst representing a conservative yet young image.
The Business Card obviously needs a field for Name, Surname, Job Title, Adress fields: Street, City, Postcode, Country, telefone and cell number, website address, etc.
We have uploaded the ai file. We trust that these are OK. If not, please advise.
Reason: We have have been busy with a client engagement. We will set the project as Guaranteed in return for the troubles we cause. Apologies for the confusion.
Thank you all for these great and creative design suggestions. The team is very happy with a number of your ideas! We will be in touch tomorrow to give individual feedback before the project closes on Friday. We look forward to working with some of you to narrow down your creations. Thank you, ROLK Investments team.
All,
Target Market(s)
Financial Services Professionals, Investors, Media, 35-70 years, mainly male, well educated
Industry/Entity Type
Conservative
Requirements
Must have
- We must make use of our logo and potential tagline 'Venture Partner in Asset Management' as we are establishing a new Brand and new company in the market.
We can use 'ROLK', 'ROLK Investments', and 'ROLK Investments'+tagline 'Venture Partner in Asset Management' or simply the four-colour swoosh plus the name of the company as part of the text. (see files)
All design elements are available in black or grey-scale if required. (grey scale swoosh attached).
Due to regulation we must have the following wording on the card in small print 'ROLK Investments is an Appointed Representative of Brambury Monetary Ventures Limited, which is authorised by the Pemberton Oversight Board'.
Nice to have
- We would consider designs that make use of different printing techniques such embossing/debossing, UV spot etc.
We attach our colour palette in the files section for your reference.
Should not have
- The font we use for our company name is 'EXO' so do not use a font style that clashes with the corporate fonts, please.
Do not use other design elements than the ones we provide in the file library as part of this project.

```html
<!DOCTYPE html>
<html lang="en">
<head>
<meta charset="utf-8">
<title>ROLK Investments – Business Card</title>
<link rel="stylesheet" href="https://fonts.googleapis.com/css2?family=Exo+2:ital,wght@0,400;0,500;1,400;1,500&display=swap">
<style>
  :root {
    --bg: #e7e4e1;
    --card: #ffffff;
    --ink: #3a3b3d;
    --ink-soft: #6b6d70;
    --green: #7ab828;
    --pink: #d8286e;
    --rule: #d9d9d9;
    --strip: #ececec;
    --bar: #8a8c8f;
    --mark: #c9c9c9;
  }
  * { margin: 0; padding: 0; box-sizing: border-box; }
  html, body {
    width: 1200px; height: 867px; overflow: hidden;
    background: var(--bg);
    font-family: "Exo 2", sans-serif;
    color: var(--ink);
  }
  .sheet {
    position: relative; width: 1200px; height: 867px;
    display: flex; align-items: center; justify-content: center; gap: 40px;
  }
  .card {
    position: relative; width: 540px; height: 300px;
    background: var(--card); border-radius: 12px;
    box-shadow: 0 6px 18px rgba(0,0,0,.12);
    overflow: hidden;
  }

  /* Front */
  .front { display: flex; align-items: center; justify-content: center; gap: 36px; }
  .front .brand-dot {
    width: 150px; height: 150px; border-radius: 50%; background: var(--mark);
  }
  .front .brand-name {
    font-size: 40px; font-weight: 500; color: var(--ink); line-height: 1;
  }

  /* Back */
  .back .brand {
    position: absolute; left: 36px; top: 34px;
    display: flex; align-items: center; gap: 12px;
  }
  .back .brand-dot { width: 34px; height: 34px; border-radius: 50%; background: var(--mark); }
  .back .brand-name { font-size: 26px; font-weight: 500; color: var(--ink); }

  .person { position: absolute; left: 46px; top: 150px; width: 180px; }
  .person-name {
    font-size: 23px; font-weight: 400; color: var(--ink);
    padding-bottom: 3px; border-bottom: 1px solid var(--rule);
  }
  .person-role { font-size: 15px; font-style: italic; color: var(--green); margin-top: 1px; }

  .contact {
    position: absolute; right: 42px; top: 110px;
    text-align: right; font-size: 13px; color: var(--ink-soft); line-height: 1.25;
  }
  .contact .address { margin-bottom: 10px; }
  .contact .group { margin-bottom: 10px; }
  .contact-line { display: flex; justify-content: flex-end; align-items: center; gap: 6px; }
  .contact-line svg { width: 9px; height: 9px; flex: none; }

  .side-bar {
    position: absolute; right: 14px; top: 100px; width: 9px; height: 100px;
    background: linear-gradient(to right, var(--bar), #b3b5b7);
  }

  .legal {
    position: absolute; left: 0; right: 0; bottom: 0; height: 24px;
    background: var(--strip);
    font-size: 7.6px; font-style: italic; color: var(--ink-soft);
    display: flex; align-items: center; justify-content: center; white-space: nowrap;
  }
</style>
</head>
<body>
<main class="sheet">

  <section class="card front" aria-label="Card front">
    <span class="brand-dot"></span>
    <span class="brand-name">ROLK Investments</span>
  </section>

  <section class="card back" aria-label="Card back">
    <div class="brand">
      <span class="brand-dot"></span>
      <span class="brand-name">ROLK Investments</span>
    </div>

    <div class="person">
      <p class="person-name">Daniel Hart</p>
      <p class="person-role">manager</p>
    </div>

    <div class="contact">
      <p class="address">Adress line 2</p>
      <div class="group">
        <p class="contact-line">+44 00 000 000
          <svg viewBox="0 0 10 10"><path d="M2 1l2 2-1 1.5q1 2 2.5 2.5L7 6l2 2-1.5 1.5Q3 9 .5 2.5z" fill="var(--pink)"/></svg>
        </p>
        <p class="contact-line">+44 00 000 000
          <svg viewBox="0 0 10 10"><rect x="2.5" y=".5" width="5" height="9" rx="1" fill="none" stroke="var(--pink)" stroke-width="1.2"/></svg>
        </p>
      </div>
      <p class="contact-line">daniel.hart@rolk.com
        <svg viewBox="0 0 10 10"><rect x=".5" y="2" width="9" height="6" fill="var(--green)"/><path d="M.5 2l4.5 3.5L9.5 2" fill="none" stroke="#fff" stroke-width=".8"/></svg>
      </p>
      <p class="contact-line">www.rolk.com
        <svg viewBox="0 0 10 10"><circle cx="5" cy="5" r="4.5" fill="var(--green)"/><path d="M1 5h8M5 .5q-2.5 4.5 0 9M5 .5q2.5 4.5 0 9" fill="none" stroke="#fff" stroke-width=".6"/></svg>
      </p>
    </div>

    <span class="side-bar"></span>

    <p class="legal">ROLK Investments is an Appointed Representative of Brambury Monetary Ventures Limited, which is authorised by the Pemberton Oversight Board</p>
  </section>

</main>
</body>
</html>
```